Fun Trendy High End Spa Services
Business Card, Gift Certificate, Gift Certificate Envelope
I need double sided standard sized Business Card [3.5" x 2"]
We like what is in logo that was uploaded but please use your creativity. We are open to any ideas.
Simple
Lena Harbus LMT
Owner
Mobile
BP@BrightPebblo.com
BrightPebblo.com
We are open to all concepts. So please be creative. This is for Very high end spa service so it needs to look very good. We thought black paper for a base on business cards, gift certificate and GC envelope but are open to any and all ideas! Thank You! We will pick a winner early if we find the perfect design.
"The greatest wealth is health"
(Doesnt need " " on there just use your own idea and play with it.)
Here is The winning logo design. We really like the style but please feel free to be creative with it! Thank you so much!
This is the style of gift certificate that we want designed to match our business card.

```html
<!DOCTYPE html>
<html lang="en">
<head>
<meta charset="utf-8">
<title>Bright Pebblo – Stationery Set</title>
<link href="https://fonts.googleapis.com/css2?family=Josefin+Sans:wght@300&family=Cormorant+Garamond:ital,wght@1,500&family=Italianno&display=swap" rel="stylesheet">
<style>
:root{
  --stage-light:#e6e7e9;
  --stage-dark:#a9abae;
  --ink:#0d0d0d;
  --band:#1a1a1a;
  --silver:#d9dadc;
  --paper:#f7f7f7;
  --paper-shade:#dcdcdc;
  --text-light:#f2f2f2;
  --text-dark:#1c1c1c;
  --label:#2b2b2b;
  --accent:#e0127a;
  --rule:#777;
}
*{margin:0;padding:0;box-sizing:border-box}
html,body{width:1200px;height:1033px;overflow:hidden}
body{background:radial-gradient(ellipse at 50% 45%,var(--stage-light) 0%,var(--stage-dark) 100%);position:relative;font-family:"Cormorant Garamond",serif}
.piece-label{position:absolute;font:9px Arial,sans-serif;color:var(--label)}
.piece{position:absolute}
.piece svg.shape{position:absolute;inset:0;width:100%;height:100%}
.brand{position:absolute;font-family:"Josefin Sans",sans-serif;font-weight:300;color:var(--text-light);display:flex;align-items:center;white-space:nowrap}
.brand .dot{border:1.5px solid var(--text-light);border-radius:50%;margin-right:.45em}
.band-text{position:absolute;display:flex;justify-content:space-between;align-items:center;color:var(--text-light)}
.band-text .small{font:11px Arial,sans-serif}
.band-text .tagline{font-family:"Cormorant Garamond",serif;font-style:italic;font-weight:500}
/* gift card */
.gift-card{left:54px;top:33px;width:782px;height:352px}
.gift-card .brand{left:320px;top:38px;font-size:40px;line-height:1}
.gift-card .brand .dot{width:34px;height:34px}
.fields{position:absolute;left:70px;top:166px;width:640px}
.field{display:flex;align-items:flex-end;font-family:"Italianno",cursive;font-size:30px;color:var(--text-dark);height:39px}
.field .line{flex:1;border-bottom:1px solid var(--rule);margin:0 6px 9px}
.field.indent{padding-left:58px}
.gift-card .band-text{left:22px;right:22px;bottom:0;height:40px}
.gift-card .tagline{font-size:25px}
/* envelope */
.envelope{left:54px;top:544px;width:782px;height:452px}
.envelope .brand{left:318px;top:124px;font-size:42px}
.envelope .brand .dot{width:36px;height:36px}
.envelope .band-text{left:22px;right:22px;bottom:0;height:46px}
.envelope .tagline{font-size:26px}
/* business cards */
.biz{width:257px;height:140px;left:913px}
.biz .brand{font-size:19px}
.biz .brand .dot{width:16px;height:16px}
.biz-front{top:572px}
.biz-front .brand{left:76px;top:14px}
.owner{position:absolute;left:18px;top:62px;color:var(--text-light);font:8px Arial,sans-serif;line-height:1.3}
.owner .name{color:var(--accent);font-size:11px}
.contact{position:absolute;left:140px;top:62px;color:var(--text-light);font:6.5px Arial,sans-serif;line-height:1.45}
.biz-front .tagline{position:absolute;left:0;right:0;bottom:12px;text-align:center;color:var(--text-light);font-size:12px;font-style:italic}
.biz-back{top:770px}
.biz-back .brand{left:76px;top:14px}
.biz-back .tagline{position:absolute;left:0;right:0;top:84px;text-align:center;color:var(--text-light);font-size:15px;font-style:italic}
</style>
</head>
<body>

<div class="piece-label" style="left:56px;top:18px">Gift Card</div>
<section class="piece gift-card">
  <svg class="shape" viewBox="0 0 782 352" preserveAspectRatio="none" aria-hidden="true">
    <defs>
      <linearGradient id="giftPaper" x1="0" y1="0" x2="0" y2="1">
        <stop offset="0" stop-color="var(--paper)"/><stop offset="1" stop-color="var(--paper-shade)"/>
      </linearGradient>
      <radialGradient id="giftBand" cx="0.5" cy="0.2" r="0.7">
        <stop offset="0" stop-color="#4a4a4a"/><stop offset="1" stop-color="var(--ink)"/>
      </radialGradient>
      <clipPath id="giftClip"><rect width="782" height="352" rx="26"/></clipPath>
    </defs>
    <g clip-path="url(#giftClip)">
      <rect width="782" height="352" fill="url(#giftPaper)"/>
      <path d="M0 0H782V120Q560 88 380 118Q190 152 0 168Z" fill="url(#giftBand)"/>
      <path d="M0 168Q190 152 380 118Q560 88 782 120" fill="none" stroke="var(--silver)" stroke-width="3"/>
      <rect y="312" width="782" height="40" fill="var(--band)"/>
    </g>
  </svg>
  <div class="brand"><span class="dot"></span>Bright Pebblo</div>
  <div class="fields">
    <div class="field">In the amount of<span class="line"></span>&amp;<span class="line" style="flex:.35"></span></div>
    <div class="field indent">A gift for<span class="line"></span></div>
    <div class="field">Presented by<span class="line"></span></div>
  </div>
  <div class="band-text"><span class="small">555-014-2290</span><span class="tagline">Luxury In Home Spa Experience</span><span class="small">BrightPebblo.com</span></div>
</section>

<div class="piece-label" style="left:56px;top:528px">Envelop Gift Card</div>
<section class="piece envelope">
  <svg class="shape" viewBox="0 0 782 452" preserveAspectRatio="none" aria-hidden="true">
    <defs>
      <linearGradient id="envPaper" x1="0" y1="0" x2="0" y2="1">
        <stop offset="0" stop-color="var(--paper)"/><stop offset="1" stop-color="var(--paper-shade)"/>
      </linearGradient>
      <radialGradient id="envBand" cx="0.5" cy="0.35" r="0.7">
        <stop offset="0" stop-color="#555"/><stop offset="1" stop-color="var(--ink)"/>
      </radialGradient>
    </defs>
    <rect width="782" height="452" fill="url(#envPaper)"/>
    <path d="M0 0H782V150Q700 205 560 205Q400 200 230 210Q90 215 0 180Z" fill="url(#envBand)"/>
    <path d="M0 180Q90 215 230 210Q400 200 560 205Q700 205 782 150" fill="none" stroke="var(--silver)" stroke-width="3"/>
    <rect y="406" width="782" height="46" fill="var(--band)"/>
  </svg>
  <div class="brand"><span class="dot"></span>Bright Pebblo</div>
  <div class="band-text"><span class="small">555-014-2290</span><span class="tagline">The Greatest Wealth Is Health</span><span class="small">BrightPebblo.com</span></div>
</section>

<div class="piece-label" style="left:913px;top:558px">Business Card Front</div>
<section class="piece biz biz-front">
  <svg class="shape" viewBox="0 0 257 140" aria-hidden="true">
    <defs><radialGradient id="bizBg" cx="0.5" cy="0.15" r="0.8"><stop offset="0" stop-color="#4d4d4d"/><stop offset="1" stop-color="var(--ink)"/></radialGradient></defs>
    <rect width="257" height="140" rx="14" fill="url(#bizBg)"/>
    <path d="M4 54Q80 40 150 46Q210 50 253 30" fill="none" stroke="var(--silver)" stroke-width="1.6"/>
  </svg>
  <div class="brand"><span class="dot"></span>Bright Pebblo</div>
  <div class="owner"><span class="name">Lena Harbus</span> LMT<br>Owner</div>
  <div class="contact">Phone 555-014-2290<br>Email: BP@BrightPebblo.com<br>www.BrightPebblo.com</div>
  <div class="tagline">The Greatest Wealth Is Health</div>
</section>

<div class="piece-label" style="left:913px;top:755px">Business Card Back</div>
<section class="piece biz biz-back">
  <svg class="shape" viewBox="0 0 257 140" aria-hidden="true">
    <rect width="257" height="140" rx="14" fill="url(#bizBg)"/>
    <path d="M4 54Q80 40 150 46Q210 50 253 30" fill="none" stroke="var(--silver)" stroke-width="1.6"/>
  </svg>
  <div class="brand"><span class="dot"></span>Bright Pebblo</div>
  <div class="tagline">Luxury In Home Spa Experience</div>
</section>

</body>
</html>
```